Stationary Package for New Bookkeeping Business

We need the following stationary designs:

- Business Card
- Letterhead
- With Comps
- Envelopes
- Paper Folder
- Email Signature

We will provide accounting and bookkeeping services to small business. We would like have the main color as blue and have a modern professional look.

Variations of colour and shades of blue welcome
Preference for deeper darker blue - navy

Variations of font in logo also welcome

Requirements
Must have
• Rosalind
B.Bus (Accounting)
Registered BAS Agent

Phone 0491 382 507
Post PO Box 947 Kelmora NSW 2768

Email rosalind@tarwinledgers.com

Business Card to be bold and eye catching

Should not have
• Letter head to not have too much colour on it

```html
<!DOCTYPE html>
<html lang="en">
<head>
<meta charset="utf-8">
<title>Tarwin Ledgers Letterhead</title>
<link href="https://fonts.googleapis.com/css2?family=Questrial&display=swap" rel="stylesheet">
<style>
  :root {
    --backdrop: #e9eaec;
    --paper: #f7f7f8;
    --navy: #1d3566;
    --slate: #6b6e78;
    --text-grey: #5d6069;
    --faint: #eeeef0;
  }
  * { margin: 0; padding: 0; box-sizing: border-box; }
  html, body {
    width: 1200px; height: 936px; overflow: hidden;
    background: var(--backdrop);
    font-family: "Questrial", "Century Gothic", sans-serif;
  }
  .letterhead {
    position: absolute;
    left: 310px; top: 48px;
    width: 580px; height: 840px;
    background: var(--paper);
    box-shadow: 0 2px 8px rgba(0,0,0,0.12);
  }
  .header-accent {
    position: absolute;
    left: 300px; top: 0;
    width: 180px; height: 40px;
    background: var(--faint);
  }
  .brand {
    position: absolute;
    left: 48px; top: 70px;
    display: flex; align-items: center; gap: 8px;
  }
  .brand-square {
    width: 30px; height: 30px;
    background: var(--navy);
  }
  .brand-name {
    color: var(--navy);
    font-size: 17px;
    line-height: 1.05;
  }
  .web-address {
    position: absolute;
    right: 40px; top: 740px;
    font-size: 8px;
    color: var(--text-grey);
  }
  .web-rule {
    position: absolute;
    right: 40px; top: 752px;
    width: 62px; height: 4px;
    background: var(--slate);
  }
  .contact {
    position: absolute;
    left: 48px; top: 768px;
    font-size: 8px;
    color: var(--text-grey);
    line-height: 1.5;
  }
  .contact-row { display: flex; gap: 10px; align-items: center; }
  .contact-item { display: inline-flex; align-items: center; gap: 3px; }
  .contact-item svg { width: 8px; height: 8px; }
  .footer-rule {
    position: absolute;
    left: 48px; top: 800px;
    width: 410px; height: 3px;
    background: var(--navy);
  }
</style>
</head>
<body>
  <main class="letterhead">
    <div class="header-accent"></div>

    <div class="brand">
      <div class="brand-square"></div>
      <div class="brand-name">Tarwin<br>Ledgers</div>
    </div>

    <div class="web-address">www.<strong>tarwinledgers</strong>.com</div>
    <div class="web-rule"></div>

    <div class="contact">
      <div class="contact-line">PO Box 947 Kelmora NSW 2768</div>
      <div class="contact-row">
        <span class="contact-item">
          <svg viewBox="0 0 10 10"><circle cx="5" cy="5" r="5" fill="#1d3566"/><path d="M3 2.5l1 1-0.6 0.8c0.4 0.9 1 1.5 1.9 1.9l0.8-0.6 1 1-0.7 1C4.8 7.4 2.6 5.2 2.5 3.2z" fill="#fff"/></svg>
          0491 382 507
        </span>
        <span class="contact-item">
          <svg viewBox="0 0 10 10"><circle cx="5" cy="5" r="5" fill="#1d3566"/><rect x="2.5" y="4" width="5" height="3" fill="#fff"/><rect x="3.5" y="2.5" width="3" height="1.5" fill="#fff"/></svg>
          0491 382 508
        </span>
        <span class="contact-item">
          <svg viewBox="0 0 10 10"><circle cx="5" cy="5" r="5" fill="#1d3566"/><rect x="2.3" y="3.2" width="5.4" height="3.6" fill="#fff"/><path d="M2.3 3.2L5 5.3 7.7 3.2" stroke="#1d3566" stroke-width="0.6" fill="none"/></svg>
          rosalind@tarwinledgers.com
        </span>
      </div>
    </div>
    <div class="footer-rule"></div>
  </main>
</body>
</html>
```